Marketing Brochures and Sales Sheets

Looking for product brochures for our line of touch screens.

For this design we want to incorporate our new color scheme(attached). We are a tech company that specializes in high performance touch screens. This flyer will be the first of 20 or more.

Target Market(s)

AV companies and businesses looking for touch screen solutions

Industry/Entity Type

Technology Equipment

Requirements
Nice to have
• You can check out our competitors flyers. They are called Varolux

```html
<!DOCTYPE html>
<html lang="en">
<head>
<meta charset="utf-8">
<title>Tilted Touch Screen Tables – Brochure</title>
<link rel="stylesheet" href="https://fonts.googleapis.com/css2?family=Josefin+Sans:wght@300;400&display=swap">
<style>
  :root {
    --navy: #131b33;
    --navy-deep: #0f1629;
    --blue: #2f6bc2;
    --blue-bright: #3d7ed6;
    --mist: #bccddb;
    --mist-soft: #c7d6e2;
    --paper: #ffffff;
    --backdrop: #e7e9ec;
    --ink-light: #e9eef6;
    --ink-dark: #1b2238;
  }
  * { box-sizing: border-box; margin: 0; padding: 0; }
  html, body { width: 1200px; height: 960px; overflow: hidden; }
  body {
    background: var(--backdrop);
    font-family: "Josefin Sans", sans-serif;
    font-weight: 300;
    position: relative;
  }
  .panel {
    position: absolute;
    left: 280px;
    width: 640px;
    height: 452px;
    overflow: hidden;
  }
  .panel--outside { top: 20px; background: var(--navy); }
  .panel--inside { top: 488px; background: var(--paper); }
  .panel svg.shapes { position: absolute; inset: 0; }

  /* Outside spread */
  .pitch {
    position: absolute;
    left: 12px; top: 14px;
    width: 196px;
    color: var(--ink-light);
  }
  .pitch__title {
    font-size: 14.5px;
    line-height: 1.18;
    font-weight: 300;
    text-transform: uppercase;
    margin-bottom: 32px;
  }
  .pitch__list {
    list-style: none;
    font-size: 10.6px;
    line-height: 1.36;
    text-align: right;
  }
  .pitch__list li::before { content: "\2022"; }
  .contact {
    position: absolute;
    left: 212px; top: 286px;
    width: 212px; height: 130px;
    display: flex; flex-direction: column; justify-content: center;
    text-align: center;
    color: var(--ink-dark);
    font-size: 11.5px;
    line-height: 1.3;
  }
  .contact__web { margin-top: 8px; }
  .brand-name {
    position: absolute;
    left: 424px; top: 286px;
    width: 216px; height: 130px;
    display: flex; align-items: center; justify-content: center;
    color: var(--blue);
    font-size: 26px;
    font-weight: 400;
  }
  .tagline {
    position: absolute;
    right: 10px; bottom: 10px;
    color: var(--ink-light);
    font-size: 12px;
    text-transform: uppercase;
  }

  /* Inside spread */
  .spec-table {
    position: absolute;
    left: 0; top: 14px;
    width: 336px;
    border-collapse: collapse;
    table-layout: fixed;
    font-size: 11.5px;
    text-align: center;
  }
  .spec-table th, .spec-table td {
    border: 1px solid var(--navy);
    height: 42px;
    line-height: 1.1;
    padding: 0 1px;
  }
  .spec-table .spec-label {
    width: 68px;
    background: var(--mist);
    color: var(--ink-dark);
    font-weight: 300;
  }
  .spec-table td { background: var(--blue); color: var(--ink-light); }
  .spec-table td.spec-small { font-size: 9px; }
  .spec-table td.spec-tight { font-size: 10px; letter-spacing: -0.3px; }
  .spec-table .spec-head td,
  .spec-table .spec-price td { background: var(--navy-deep); color: var(--paper); font-size: 14px; }
  .spec-table .spec-head th { height: 44px; }
  .spec-table .spec-aspect td { color: var(--mist-soft); }

  .product-shots {
    position: absolute;
    left: 430px; top: 10px;
    width: 200px; height: 190px;
    background: radial-gradient(circle at 50% 45%, #8b8f96 0%, #c9ccd1 45%, var(--paper) 75%);
  }
  .section-title {
    position: absolute;
    left: 414px; top: 300px;
    width: 215px;
    text-align: center;
    color: var(--ink-light);
    font-size: 27px;
    line-height: 1.2;
    text-transform: uppercase;
  }
</style>
</head>
<body>

<section class="panel panel--outside">
  <svg class="shapes" width="640" height="452" viewBox="0 0 640 452">
    <defs>
      <linearGradient id="tableShotTone" x1="0" y1="0" x2="1" y2="1">
        <stop offset="0" stop-color="#3a4150"/>
        <stop offset="0.5" stop-color="#9fb4c7"/>
        <stop offset="1" stop-color="#6c6259"/>
      </linearGradient>
      <linearGradient id="deskShotTone" x1="0" y1="0" x2="1" y2="0">
        <stop offset="0" stop-color="#5a5350"/>
        <stop offset="0.6" stop-color="#c9d3dc"/>
        <stop offset="1" stop-color="#9aa6b2"/>
      </linearGradient>
    </defs>
    <polygon points="416,0 640,0 640,286 470,286 416,190" fill="url(#tableShotTone)" role="img" aria-label="Photo of a tilted touch screen table showing a car on its display"/>
    <polygon points="416,84 640,28 640,42 416,100" fill="var(--navy)"/>
    <polygon points="416,236 640,150 640,164 430,246" fill="var(--navy)"/>
    <polygon points="0,334 212,296 212,412 0,412" fill="url(#deskShotTone)" role="img" aria-label="Photo of a hand using a touch screen desk"/>
    <rect x="212" y="286" width="212" height="130" fill="var(--mist-soft)"/>
    <polygon points="424,286 640,286 640,416 424,416" fill="var(--mist)"/>
  </svg>

  <div class="pitch">
    <h1 class="pitch__title">Why is our tilted touch screen the best option for you?</h1>
    <ul class="pitch__list">
      <li>It has an easy access</li>
      <li>It is simple to use</li>
      <li>Accomodated to be used for both short and long periods of time</li>
      <li>The 20 degree tilt is perfect for displaying content in landscape mode</li>
      <li>It makes a perfect standing desk</li>
      <li>Latest technological update for industries which use registration and sign-ups on daily basis in their business</li>
    </ul>
  </div>

  <address class="contact">
    <span>Lumatab Systems, Inc.</span>
    <span>4180 Meridian Pkwy, Dayton,</span>
    <span>OH 45402</span>
    <span>555.014.2287</span>
    <span class="contact__web">www.lumatabsystems.com</span>
  </address>

  <div class="brand-name">Lumatab Systems</div>
  <p class="tagline">Tilted touch screen tables</p>
</section>

<section class="panel panel--inside">
  <svg class="shapes" width="640" height="452" viewBox="0 0 640 452">
    <polygon points="336,150 432,172 432,258 336,266" fill="var(--mist)" opacity="0.85"/>
    <polygon points="414,222 629,296 629,452 414,452" fill="var(--blue-bright)"/>
    <polygon points="506,262 629,212 629,300" fill="var(--navy)"/>
  </svg>

  <table class="spec-table">
    <tr class="spec-head"><th class="spec-label">Screen Size</th><td>42"</td><td>46"</td><td>55"</td><td>65"</td></tr>
    <tr class="spec-aspect"><th class="spec-label">Aspect Ratio</th><td>16:09</td><td>16:09</td><td>16:09</td><td>16:09</td></tr>
    <tr><th class="spec-label">Dimensions</th><td class="spec-small">38.39"<br>x22.63"<br>x3.46"</td><td class="spec-small">43.31"<br>x25.77"<br>x3.50"</td><td class="spec-small">50.96"<br>x30.13"<br>x3.50"</td><td class="spec-small">60.25"<br>x35.65"<br>x3.50"</td></tr>
    <tr><th class="spec-label">Active Area</th><td class="spec-small">36.53"<br>x20.55"</td><td class="spec-small">40.15"<br>x22.62"</td><td class="spec-small">42.62"<br>x26.68"</td><td class="spec-small">56.31"<br>x31.74"</td></tr>
    <tr><th class="spec-label">Resolution</th><td class="spec-tight">1920x1080px</td><td class="spec-tight">1920x1080px</td><td>4K</td><td>4K</td></tr>
    <tr><th class="spec-label">Touch Sensor</th><td>PCAP</td><td>PCAP</td><td>PCAP</td><td>PCAP</td></tr>
    <tr><th class="spec-label">Touch Points</th><td></td><td>12</td><td>50</td><td>50</td></tr>
    <tr><th class="spec-label">Touch Glass</th><td>4 mm</td><td>5 mm</td><td>5 mm</td><td>5 mm</td></tr>
    <tr><th class="spec-label">Luminance</th><td>400<br>cd/m2</td><td>500<br>cd/m2</td><td>500<br>cd/m2</td><td>450<br>cd/m2</td></tr>
    <tr class="spec-price"><th class="spec-label">Price</th><td>$ 5,499</td><td>$ 6,480</td><td>$ 7,290</td><td>$ 8,850</td></tr>
  </table>

  <div class="product-shots" role="img" aria-label="Product photos of three tilted touch screen table models on metal stands"></div>

  <h2 class="section-title">Main<br>product<br>information</h2>
</section>

</body>
</html>
```